Qorvel Amusements business cards

double sided cards
black cards with gold lettering

need front side to say -

Qorvel Amusements(larger font)
Live music for every event
(centered)

back side to say -

qorvelamusements.example
info@qorvelamusements
(888)555-0147
(centered)

then along the backside border, wrapping the sides and bottom it should list the bands...

Harborline Mixed Show Band-The Neon Drifters 80s band - Velvet Anchor Dock Society -Elmgrove Prep 90s Band - Pulse Grid - Skylark Waltz Orchestra Jazz - Take The Mic Tonight Karaoke

(the artwork uploaded will give you an idea of the gold and black style I am going for please)

Target Market(s)

event and wedding professional planners and event clients including brides and grooms

Industry/Entity Type

Events

Contact Information for Business Card

black with gold lettering, i WOULD LIKE TO GO HIGH END WITH THE MATERIALS THAT i print on so I am considering gold leaf

Font styles to use
Serif

Colors
ffc214
ffcf3e

Requirements
Must have
• gold letters
Nice to have
• sharp lines
Should not have
• anything too decorative

```html
<!DOCTYPE html>
<html lang="en">
<head>
<meta charset="utf-8">
<title>Qorvel Amusements – Business Cards</title>
<link rel="stylesheet" href="https://fonts.googleapis.com/css2?family=Cormorant+Garamond:wght@500;600&display=swap">
<style>
  :root {
    --backdrop: #3a3a3a;
    --card-black: #0d0c0b;
    --card-edge: #1c1a18;
    --gold: #ffc214;
    --gold-soft: #ffcf3e;
    --white: #f4f1ea;
    --serif: "Cormorant Garamond", Georgia, serif;
  }
  * { box-sizing: border-box; margin: 0; padding: 0; }
  html, body {
    width: 1200px; height: 873px; overflow: hidden;
    background: var(--backdrop);
  }
  .canvas {
    position: relative; width: 1200px; height: 873px;
    background: radial-gradient(ellipse at 50% 45%, #4a4a4a 0%, var(--backdrop) 70%);
  }
  .card {
    position: absolute; width: 620px; height: 354px;
    border-radius: 16px;
    background: radial-gradient(ellipse at 40% 35%, var(--card-edge) 0%, var(--card-black) 75%);
    box-shadow: 0 18px 40px rgba(0,0,0,.55);
    font-family: var(--serif);
    color: var(--gold);
    text-align: center;
  }
  .card--front { left: 80px; top: 40px; }
  .card--back { left: 500px; top: 470px; }

  /* front */
  .brand {
    position: absolute; left: 0; right: 0; top: 118px;
    display: flex; align-items: center; justify-content: center; gap: 14px;
  }
  .brand__mark {
    width: 16px; height: 16px; background: var(--gold);
  }
  .brand__name {
    font-size: 50px; font-weight: 600; letter-spacing: 1px; color: var(--gold);
  }
  .tagline {
    position: absolute; left: 0; right: 0; top: 196px;
    display: flex; align-items: center; justify-content: center; gap: 14px;
    font-size: 15px; font-weight: 600; letter-spacing: 5px;
    text-transform: uppercase; color: var(--white);
  }
  .tagline__rule { width: 70px; height: 1px; background: var(--gold); }

  /* back */
  .contact {
    position: absolute; left: 0; right: 0; top: 62px;
    font-size: 14px; font-weight: 600;
  }
  .contact__row {
    display: flex; justify-content: center; gap: 46px; align-items: center;
  }
  .contact__item { display: inline-flex; align-items: center; gap: 7px; }
  .contact__icon { width: 15px; height: 12px; fill: var(--gold); }
  .contact__web {
    margin-top: 14px; font-size: 17px; letter-spacing: 7px;
  }
  .bands {
    position: absolute; left: 0; right: 0; top: 196px;
    list-style: none; font-size: 19px; font-weight: 600; line-height: 1.55;
    color: var(--gold-soft);
  }
  .bands__sep { margin: 0 10px; color: var(--gold); }
</style>
</head>
<body>
<main class="canvas">

  <section class="card card--front" aria-label="Card front">
    <div class="brand">
      <span class="brand__mark"></span>
      <span class="brand__name">Qorvel Amusements</span>
    </div>
    <p class="tagline">
      <span class="tagline__rule"></span>
      Live music for every event
      <span class="tagline__rule"></span>
    </p>
  </section>

  <section class="card card--back" aria-label="Card back">
    <div class="contact">
      <div class="contact__row">
        <span class="contact__item">
          <svg class="contact__icon" viewBox="0 0 16 12" aria-hidden="true">
            <path d="M1 4 Q8 -1 15 4 L13 6 L11 4.5 L11 3.5 Q8 2.5 5 3.5 L5 4.5 L3 6 Z"/>
            <rect x="3" y="6.5" width="10" height="5" rx="1"/>
          </svg>
          (888)555-0147
        </span>
        <span class="contact__item">
          <svg class="contact__icon" viewBox="0 0 16 12" aria-hidden="true">
            <rect x="0" y="0" width="16" height="12" rx="1"/>
            <path d="M0.5 0.8 L8 7 L15.5 0.8" fill="none" stroke="#0d0c0b" stroke-width="1.2"/>
          </svg>
          info@qorvelamusements
        </span>
      </div>
      <p class="contact__web">www.qorvelamusements.example</p>
    </div>
    <ul class="bands">
      <li>Harborline Mixed Show Band<span class="bands__sep">|</span>Take The Mic Tonight Karaoke</li>
      <li>The Neon Drifters 80s band<span class="bands__sep">|</span>Velvet Anchor Dock Society</li>
      <li>Elmgrove Prep 90s Band<span class="bands__sep">|</span>Pulse Grid<span class="bands__sep">|</span>Skylark Waltz Orchestra Jazz</li>
    </ul>
  </section>

</main>
</body>
</html>
```